Food Safety Consultancy Flyer Design

We need a flyer design for a new company called KLS Training. New food safety regulations are coming into effect for all food operators in March 2016. My company provides training and resources to support food operators during the transition onto the new Kitchen Ledger Scheme. For the designs we would like to see any of the colours used from the logo which is attached. The flyer will be letting operators know that there are new regulations and we are here to help. Our company offers three packages: 1. Videos (training videos) 2. Webinars and Workshop 3. One-on-one mentoring. Our websites main colour used is the green colour from the logo.
Food service operators: cafes, restaurants etc.
Hospitality

```html
<!DOCTYPE html>
<html lang="en">
<head>
<meta charset="utf-8">
<title>KLS Training – Flyer</title>
<link rel="stylesheet" href="https://fonts.googleapis.com/css2?family=Open+Sans:wght@400;700&family=Cinzel:wght@400&display=swap">
<style>
  :root {
    --page-bg: #e9e6e1;
    --paper: #ffffff;
    --navy: #1b3a8c;
    --ink: #1f2a3a;
    --body-grey: #5a5a5a;
    --mist-top: #d6d6d6;
    --mist-bottom: #eeeeee;
    --orange: #f7a21b;
    --green: #3cf01a;
    --blue: #2d7ff5;
    --divider: #9a9a9a;
    --strip: #d2d2d2;
  }
  * { box-sizing: border-box; margin: 0; padding: 0; }
  html, body { width: 1200px; height: 1000px; overflow: hidden; }
  body { background: var(--page-bg); font-family: "Open Sans", Arial, sans-serif; position: relative; }

  .flyer {
    position: absolute; left: 260px; top: 20px;
    width: 680px; height: 960px;
    background: var(--paper);
    box-shadow: 0 6px 24px rgba(0,0,0,.18);
    overflow: hidden;
  }

  /* Header / wordmark */
  .brand {
    height: 150px; display: flex; align-items: center; justify-content: center; gap: 18px;
  }
  .brand-dot { width: 46px; height: 46px; border-radius: 50%; background: var(--green); }
  .brand-name {
    font-family: "Open Sans", Arial, sans-serif; font-weight: 700;
    font-size: 52px; letter-spacing: 4px; color: var(--ink); text-transform: uppercase;
  }

  /* Intro band */
  .intro-photo {
    position: absolute; left: 0; top: 150px; width: 680px; height: 690px;
    background: linear-gradient(180deg, var(--mist-top), var(--mist-bottom));
  }
  .columns {
    position: absolute; left: 0; top: 150px; width: 680px; height: 650px;
    display: grid; grid-template-columns: repeat(3, 1fr);
  }
  .column { position: relative; display: flex; flex-direction: column; min-width: 0; }
  .column + .column { border-left: 2px dashed var(--divider); }

  .column-intro { height: 320px; flex: none; padding: 24px 14px 0; text-align: center; }
  .intro-heading {
    color: var(--navy); font-weight: 700; font-size: 18px; line-height: 1.3; text-transform: uppercase;
  }
  .intro-heading--large { font-size: 21px; line-height: 1.45; padding: 14px 8px 0; }
  .intro-heading .date { text-transform: none; }
  .intro-text { color: var(--body-grey); font-size: 15.5px; line-height: 1.35; margin-top: 4px; }
  .topic-list { list-style: none; margin-top: 10px; text-align: center; color: var(--body-grey); font-size: 14.5px; line-height: 1.35; }
  .topic-list li { position: relative; padding-left: 14px; margin-bottom: 3px; }
  .topic-list li::before {
    content: ""; position: absolute; left: 4px; top: 6px;
    width: 9px; height: 9px; border-radius: 50%; background: #c4c4c4;
  }

  /* Package panels */
  .package {
    flex: 1; position: relative; text-align: center;
    padding: 114px 16px 0;
  }
  .package--video { background: var(--orange); }
  .package--webinar { background: var(--green); }
  .package--mentor { background: var(--blue); }
  .package-badge {
    position: absolute; left: 50%; top: -40px; transform: translateX(-50%);
    width: 140px; height: 140px; border-radius: 50%;
    background: var(--paper); border: 8px solid #f4f4f4;
    display: flex; align-items: center; justify-content: center;
  }
  .package-text {
    font-family: "Cinzel", Georgia, serif; font-size: 16px; line-height: 1.22;
    color: var(--ink);
  }
  .package--mentor .package-text { color: #14213d; }

  .strip { position: absolute; left: 0; top: 800px; width: 680px; height: 40px; background: var(--strip); opacity: .6; }

  /* Footer */
  .contact {
    position: absolute; left: 0; top: 840px; width: 680px; height: 120px; background: var(--paper);
    display: flex; justify-content: space-between; align-items: flex-start;
    padding: 22px 30px 0;
    font-size: 17px; color: var(--navy);
  }
  .contact-item { display: flex; align-items: center; gap: 10px; }
  .contact-item--email { margin-top: 36px; }
</style>
</head>
<body>
  <main class="flyer">
    <header class="brand">
      <span class="brand-dot"></span>
      <span class="brand-name">KLS Training</span>
    </header>

    <div class="intro-photo" role="img" aria-label="Soft, faded photograph of cutlery on a table"></div>

    <section class="columns">
      <div class="column">
        <div class="column-intro">
          <h2 class="intro-heading">The Food Act 2014 comes into force <span class="date">on 1 March 2016</span></h2>
          <p class="intro-text">Food service and food retailers will be on Kitchen Ledger Schemes – documentation of processes and risk management to produce safe and suitable food.</p>
        </div>
        <div class="package package--video">
          <div class="package-badge">
            <svg width="78" height="60" viewBox="0 0 78 60" aria-hidden="true">
              <rect x="2" y="2" width="74" height="56" rx="3" fill="#111"/>
              <rect x="12" y="12" width="54" height="36" fill="#fff"/>
              <g fill="#fff">
                <rect x="4" y="5" width="5" height="4"/><rect x="4" y="17" width="5" height="4"/><rect x="4" y="29" width="5" height="4"/><rect x="4" y="41" width="5" height="4"/><rect x="4" y="51" width="5" height="4"/>
                <rect x="69" y="5" width="5" height="4"/><rect x="69" y="17" width="5" height="4"/><rect x="69" y="29" width="5" height="4"/><rect x="69" y="41" width="5" height="4"/><rect x="69" y="51" width="5" height="4"/>
              </g>
              <polygon points="33,21 33,39 48,30" fill="#111"/>
            </svg>
          </div>
          <p class="package-text">Animated training videos of the KLS 6 month subscription Translated into Mandarin, Japanese, Korean and Hindi</p>
        </div>
      </div>

      <div class="column">
        <div class="column-intro">
          <h2 class="intro-heading">Your reputation is our business with up-to-date knowledge on:</h2>
          <ul class="topic-list">
            <li>Kitchen Ledger Scheme requirements</li>
            <li>New Food Grading system</li>
            <li>Verification expectations</li>
            <li>New Fees</li>
          </ul>
        </div>
        <div class="package package--webinar">
          <div class="package-badge">
            <svg width="84" height="66" viewBox="0 0 84 66" aria-hidden="true">
              <rect x="4" y="4" width="70" height="46" rx="3" fill="#111"/>
              <rect x="10" y="10" width="58" height="34" fill="#fff"/>
              <rect x="34" y="50" width="10" height="8" fill="#111"/>
              <rect x="22" y="58" width="34" height="5" rx="2" fill="#111"/>
            </svg>
          </div>
          <p class="package-text">A range of webinars at times to suit the hospitality industry and half day training workshops. 6 month subscription to the video library is included</p>
        </div>
      </div>

      <div class="column">
        <div class="column-intro">
          <h2 class="intro-heading intro-heading--large">Let us help you transition and understand all there is to know!</h2>
        </div>
        <div class="package package--mentor">
          <div class="package-badge">
            <svg width="80" height="80" viewBox="0 0 80 80" role="img" aria-label="Icon of two people for one-on-one mentoring">
              <circle cx="40" cy="40" r="34" fill="#dcdcdc"/>
            </svg>
          </div>
          <p class="package-text">We come to you and go through the KLS page-by-page</p>
        </div>
      </div>
    </section>

    <div class="strip"></div>

    <footer class="contact">
      <span class="contact-item">
        <svg width="22" height="22" viewBox="0 0 22 22" aria-hidden="true">
          <circle cx="11" cy="11" r="10" fill="var(--navy)"/>
          <ellipse cx="11" cy="11" rx="4" ry="10" fill="none" stroke="#fff" stroke-width="1.3"/>
          <line x1="1" y1="11" x2="21" y2="11" stroke="#fff" stroke-width="1.3"/>
        </svg>
        www.klstraining.co.nz
      </span>
      <span class="contact-item contact-item--email">
        <svg width="22" height="16" viewBox="0 0 22 16" aria-hidden="true">
          <rect x="0" y="0" width="22" height="16" rx="2" fill="var(--navy)"/>
          <polyline points="2,2 11,9 20,2" fill="none" stroke="#fff" stroke-width="1.6"/>
        </svg>
        info@klstraining.co.nz
      </span>
    </footer>
  </main>
</body>
</html>
```